90 Day Landing Page for Online Coaching

Need a website design that’s gonna be used for an online coaching landing page (details in the WORD document). The colors/design can be complimentary to the program called, The Harvest Ledger Method; the banners are attached in the document
There are alot of extra photos that you can use but none of them are required; use as needed.
We don’t have the URL yet, but we intend to use a single landing page.

Target Market(s)

for men and women looking to launch a business

Industry/Entity Type

business consulting

Requirements
Must have
• the copy attached

```html
<!DOCTYPE html>
<html lang="en">
<head>
<meta charset="utf-8">
<title>The Harvest Ledger Method – Landing Page</title>
<link href="https://fonts.googleapis.com/css2?family=Montserrat:wght@400;500;600;700;800&display=swap" rel="stylesheet">
<style>
:root{
  --stage:#c9c9c9;
  --navy:#0b3a74;
  --band:#0e4a8e;
  --steel:#2f6ea6;
  --sky:#2b9be0;
  --orange:#f5a01a;
  --pink:#e6457a;
  --pale:#e7f2fc;
  --ink:#1f2a3a;
  --muted:#5d6878;
  --white:#ffffff;
}
*{box-sizing:border-box;margin:0;padding:0}
html,body{width:1200px;height:1200px;overflow:hidden}
body{background:var(--stage);font-family:"Montserrat",sans-serif;color:var(--ink)}
.page{position:absolute;left:510.5px;top:23px;width:720px;height:4645px;transform:scale(.2485);transform-origin:0 0;background:var(--white);overflow:hidden}
section{position:relative;padding:0 78px}
h2{font-size:22px;font-weight:500;line-height:1.15;color:var(--navy)}
h2 .hl{color:var(--sky)}
h2 .or{color:var(--orange)}
p{font-size:7.5px;line-height:1.6;color:var(--muted)}
.btn{display:inline-block;background:var(--orange);color:#fff;font-size:7px;font-weight:700;padding:6px 18px;border-radius:3px}
.ph{border-radius:10px}
.pale{background:var(--pale)}
.tick{width:9px;height:9px;flex:none}
.row{display:flex}

.hero{height:365px;background:linear-gradient(180deg,#e3f0fc,#eaf4fd)}
.nav{height:58px;display:flex;align-items:center;gap:12px}
.brand{display:flex;align-items:center;gap:5px;font-size:8px;font-weight:700;color:var(--navy);width:180px}
.brand i{width:10px;height:10px;background:var(--sky);display:block}
.nav a{font-size:6px;color:var(--ink);text-decoration:none}
.nav .sp{flex:1}
.nav .join{background:var(--navy);color:#fff;padding:7px 18px;border-radius:3px;font-weight:600}
.hero-body{display:flex;justify-content:space-between;align-items:center;height:290px}
.hero-copy{width:300px}
.hero-copy .kick{font-size:22px;font-weight:600;color:var(--navy)}
.hero-copy h1{font-size:28px;font-weight:700;line-height:1.1;color:var(--sky);margin-bottom:10px}
.hero-copy h1 b{color:var(--orange)}
.hero-copy p{margin-bottom:14px}
.banner{width:237px;height:250px;border-radius:10px;background:linear-gradient(160deg,#1a5fb4,#0a3370);display:flex;align-items:center;justify-content:center}
.play{width:30px;height:30px;border-radius:50%;background:rgba(255,255,255,.85);display:flex;align-items:center;justify-content:center}

.sound{height:305px;display:flex;gap:70px;align-items:center}
.sound .photo{width:206px;height:265px;background:linear-gradient(135deg,#f6c6d2,#c7303f 55%,#d9d4cc)}
.sound ul{list-style:none;margin:10px 0 14px}
.sound li{display:flex;gap:7px;align-items:flex-start;font-size:6.5px;color:var(--ink);margin-bottom:9px;width:260px}

.alone{height:330px;display:flex;justify-content:space-between;align-items:center}
.alone .copy{width:250px}
.alone .copy p{margin:8px 0}
.alone .copy .more{color:var(--sky);font-size:7px}
.collage{width:193px;height:260px;background:linear-gradient(160deg,#6d8b5b,#2c3d5a 50%,#bfa77a)}

.trans{height:215px;display:flex;gap:24px;padding-top:30px}
.trans .lead{width:180px}
.trans .lead p{margin:8px 0 12px}
.cols{display:grid;grid-template-columns:1fr 1fr;gap:12px 18px;width:380px}
.cols div{display:flex;gap:6px;font-size:6px;color:var(--ink);line-height:1.5}
.enroll{position:absolute;left:282px;bottom:18px;display:flex;gap:8px;align-items:center;font-size:6px;color:var(--ink);border-top:1px solid #f4d9a8;padding-top:6px;width:360px}
.enroll .pill{background:var(--orange);color:#fff;padding:4px 10px;border-radius:10px;font-weight:700}

.wins{height:235px;text-align:center;padding-top:22px}
.wins h2{font-size:16px}
.cards4{display:grid;grid-template-columns:repeat(4,1fr);margin-top:18px;text-align:left;border:1px solid #e6e6e6}
.cards4 .c{padding:10px 8px;height:128px;position:relative;border-right:1px solid #e6e6e6}
.cards4 .c p{font-size:5.5px;color:var(--ink)}
.cards4 .c.feat{background:var(--orange)}
.cards4 .c.feat p,.cards4 .c.feat .who{color:#fff}
.cards4 .rm{font-size:5.5px;color:var(--orange);margin-top:6px}
.cards4 .feat .rm{color:#fff}
.who{position:absolute;bottom:10px;left:8px;display:flex;gap:6px;align-items:center;font-size:6px}
.who i{width:14px;height:14px;border-radius:50%;background:#7a6a60;display:block}

.future{height:228px;background:linear-gradient(120deg,var(--band),#0b3f7c);display:flex;justify-content:space-between;align-items:center}
.future .copy{color:#fff;width:330px}
.future h2{color:#fff;font-size:19px}
.future h2 .or{color:var(--orange)}
.future .copy .sub{font-size:8px;color:#fff;margin:8px 0 14px;line-height:1.3}
.outline{display:inline-block;border:1px solid #fff;color:#fff;font-size:7px;padding:5px 24px;border-radius:12px;margin-left:6px}
.future .banner{width:210px;height:210px}

.killers{height:247px;display:flex;align-items:center;gap:10px}
.killers .lead{width:190px}
.killers .lead p{margin-top:8px}
.killers .photo{width:150px;height:220px;background:linear-gradient(180deg,#f1ece6,#1d1d22 60%,#f5a01a 98%)}
.killers .list{width:215px}
.killers h4{font-size:6.5px;color:var(--orange);font-weight:700;margin:10px 0 3px}
.killers h4.b{color:var(--sky)}
.killers .list p{font-size:5.5px}

.coaches{height:188px;padding-top:22px}
.coaches .pics{display:flex;gap:20px;margin-top:16px}
.coaches .pics div{width:165px;height:95px;background:linear-gradient(135deg,#d9d2c7,#33324a)}
.tag{display:inline-block;background:var(--orange);color:#fff;font-size:9px;padding:6px 14px;position:absolute}
.coaches .side{position:absolute;right:0;top:0;width:200px;height:188px;background:linear-gradient(160deg,#8b5a3f,#d8a27b)}
.bio{height:142px;background:var(--steel);display:grid;grid-template-columns:200px 170px 190px;gap:18px;padding-top:12px}
.bio h5,.todd h5{font-size:6px;font-weight:700;color:#fff;letter-spacing:.3px}
.bio p{color:#e6efff;font-size:5.5px;line-height:1.45;margin-bottom:6px}
.todd{height:318px;display:flex;padding:0}
.todd .photo{width:220px;height:318px;background:linear-gradient(180deg,#5c6f84,#2a2d33)}
.todd .txt{flex:1;padding:18px 28px 0 10px;position:relative}
.todd .grid{display:grid;grid-template-columns:1fr 1fr;gap:24px;margin-top:36px}
.todd h5{color:var(--ink);margin:6px 0 2px}
.todd p{font-size:5.5px;line-height:1.5}
.media{height:42px;display:flex;justify-content:space-between;align-items:center;background:#fff}
.media i{display:block;width:40px;height:12px;background:#b9c2cf;border-radius:2px}

.inspire{height:430px;padding-top:18px}
.strip{display:flex;justify-content:space-between;padding:0 10px}
.strip div{width:124px;height:132px;background:linear-gradient(160deg,#a6c6df,#3b2e3a);border-radius:4px}
.inspire h2{text-align:center;font-size:16px;margin:38px 0 28px}
.inspire h2 .sm{color:var(--sky)}
.cards3{display:flex;gap:10px;justify-content:center}
.cards3 .c{width:168px;height:115px;background:#fff;border-radius:4px;text-align:center;padding:8px 12px;position:relative}
.cards3 .av{width:36px;height:36px;border-radius:50%;background:#6e4a3c;margin:0 auto 5px}
.cards3 b{font-size:5.5px;display:block;margin-bottom:4px}
.cards3 p{font-size:5.2px;color:var(--ink);line-height:1.45}
.cards3 .rm{position:absolute;right:12px;bottom:6px;font-size:5px;color:var(--orange)}

.every{height:265px;padding-top:20px}
.every h2{text-align:center;font-size:15px;color:var(--navy);margin-bottom:18px}
.every h2 .sm{color:var(--sky)}
.grid4{display:grid;grid-template-columns:repeat(4,1fr);gap:12px}
.grid4 .it{display:flex;gap:4px;margin-bottom:8px}
.grid4 b{font-size:5px;display:block}
.grid4 p{font-size:4.8px;line-height:1.4}
.rule{height:1px;background:#f5d79c;margin-top:10px}

.stories{height:262px;display:flex;gap:60px;padding-top:18px;padding-left:145px}
.stories .lead{width:150px}
.stories .lead h2{font-size:11px}
.stories .lead p{font-size:6px;margin:4px 0 12px}
.dates{background:var(--orange);border-radius:5px;padding:10px;height:80px}
.dates b{font-size:6.5px;color:#fff;display:block;margin-bottom:6px}
.dates span{display:block;font-size:5px;color:#fff;border-bottom:1px solid rgba(255,255,255,.5);padding:3px 0}
.vids .v{display:flex;gap:16px;margin-bottom:18px;align-items:flex-start}
.vids .thumb{width:88px;height:62px;background:linear-gradient(135deg,#c9b9a4,#3a3340);border-radius:4px;display:flex;align-items:center;justify-content:center}
.vids .q{font-size:5.5px;font-weight:600;width:100px}
.vids .q span{display:inline-block;background:#3cc16b;color:#fff;font-size:4.5px;padding:2px 8px;border-radius:6px;margin-top:6px;font-weight:500}

.types{height:270px;padding-left:0}
.wheelcard{position:absolute;left:130px;top:2px;width:370px;height:260px;background:#fff;border:1px solid #e3e8ef;box-shadow:0 1px 4px rgba(0,0,0,.08)}
.wheelcard h6{font-size:6.5px;text-align:center;margin-top:8px;font-weight:700}
.note{position:absolute;left:458px;top:30px;width:186px;background:var(--orange);color:#fff;font-size:6px;font-weight:600;line-height:1.5;padding:10px}

.faq{height:267px;display:flex;gap:30px;padding-top:14px}
.faq .list{width:200px}
.faq h3{font-size:9px;font-weight:500;color:var(--navy);margin-bottom:10px}
.faq b{font-size:6px;color:var(--navy);display:block}
.faq p{font-size:5.5px;margin-bottom:10px}
.fcard{width:170px;height:218px;background:#fff;margin-top:28px;position:relative}
.fcard .img{height:110px;background:linear-gradient(160deg,#d8d2cc,#b8322f)}
.fcard .date{position:absolute;left:6px;top:100px;width:26px;height:26px;border-radius:50%;background:var(--sky);color:#fff;font-size:5px;text-align:center;padding-top:7px}
.fcard b{font-size:6px;display:block;margin:24px 14px 4px}
.fcard p{font-size:5px;margin:0 14px}

.cta{height:263px;text-align:center;padding-top:38px}
.cta h2{font-size:17px;color:var(--orange);font-weight:500}
.cta h3{font-size:17px;color:var(--sky);font-weight:700;margin-top:22px;line-height:1.3}
.cta .btn{font-size:12px;padding:8px 30px;border-radius:6px;margin:12px 0 8px}
.cta p{font-size:5.5px;line-height:1.5}
.cta .yes{font-size:16px;color:var(--sky);font-weight:700;margin-top:12px}

.foot{height:263px;padding-top:12px}
.foot .row{gap:48px}
.foot .banner{width:200px;height:200px}
.foot h4{font-size:11px;color:var(--sky);font-weight:600;margin-top:56px;margin-bottom:10px}
.foot p{font-size:6px;color:var(--ink)}
.soc{display:flex;gap:5px;margin-top:12px;padding-top:8px;border-top:1px solid #bfd3e7;width:180px}
.soc i{display:block;width:12px;height:12px;border-radius:50%;border:1px solid var(--navy)}
.contact{display:flex;gap:8px;align-items:center;font-size:6px;color:var(--navy);margin-bottom:10px}
.legal{display:flex;justify-content:space-between;font-size:5.5px;margin-top:26px;color:var(--ink)}
.legal span{margin-right:10px}
</style>
</head>
<body>
<div class="page">

<section class="hero">
  <nav class="nav">
    <div class="brand"><i></i>The Harvest Ledger Method</div>
    <a>Home</a><a>Services ▾</a><a>Contact</a><a>About Us</a><a>FAQs</a>
    <span class="sp"></span>
    <a>Login</a><a class="join">Join course</a>
  </nav>
  <div class="hero-body">
    <div class="hero-copy">
      <div class="kick">It's Your Turn!</div>
      <h1>Launch <b>a</b> Million<br>Brand <b>in</b> 90 Days!</h1>
      <p>The Harvest Ledger Method program is a <b>90-Day Sprint</b> that helps you turn your idea, skill, or passion into a <b>brand that makes money — fast.</b></p>
      <span class="btn">Sign Up Today</span>
    </div>
    <div class="banner" role="img" aria-label="Program banner video featuring the two coaches">
      <div class="play"><svg width="12" height="12" viewBox="0 0 12 12"><path d="M3 1.5 10.5 6 3 10.5z" fill="#0b3a74"/></svg></div>
    </div>
  </div>
</section>

<section class="sound">
  <div class="photo ph" role="img" aria-label="Coaches posing together in a bright studio"></div>
  <div>
    <h2>Does This Sound<br><span class="hl">Like You?</span></h2>
    <ul>
      <li><svg class="tick" viewBox="0 0 10 10"><circle cx="5" cy="5" r="5" fill="#e6457a"/><path d="M2.8 5.2 4.3 6.6 7.2 3.6" stroke="#fff" fill="none" stroke-width="1.2"/></svg>You want to escape the paycheck-to-paycheck grind and build real wealth</li>
      <li><svg class="tick" viewBox="0 0 10 10"><circle cx="5" cy="5" r="5" fill="#e6457a"/><path d="M2.8 5.2 4.3 6.6 7.2 3.6" stroke="#fff" fill="none" stroke-width="1.2"/></svg>You're done working long hours to make someone else rich</li>
      <li><svg class="tick" viewBox="0 0 10 10"><circle cx="5" cy="5" r="5" fill="#e6457a"/><path d="M2.8 5.2 4.3 6.6 7.2 3.6" stroke="#fff" fill="none" stroke-width="1.2"/></svg>You have good ideas but can't figure out how to turn them into steady income</li>
      <li><svg class="tick" viewBox="0 0 10 10"><circle cx="5" cy="5" r="5" fill="#e6457a"/><path d="M2.8 5.2 4.3 6.6 7.2 3.6" stroke="#fff" fill="none" stroke-width="1.2"/></svg>You want a life where your schedule, income, and future are up to you—not someone else</li>
      <li><svg class="tick" viewBox="0 0 10 10"><circle cx="5" cy="5" r="5" fill="#e6457a"/><path d="M2.8 5.2 4.3 6.6 7.2 3.6" stroke="#fff" fill="none" stroke-width="1.2"/></svg>You want more money, but fear of failure (and bills) keeps holding you back</li>
      <li><svg class="tick" viewBox="0 0 10 10"><circle cx="5" cy="5" r="5" fill="#e6457a"/><path d="M2.8 5.2 4.3 6.6 7.2 3.6" stroke="#fff" fill="none" stroke-width="1.2"/></svg>You've tried launching a business, but it didn't work out the way you hoped</li>
    </ul>
    <span class="btn">Learn More</span>
  </div>
</section>

<section class="alone pale">
  <div class="copy">
    <h2>You're Not Alone. <span class="hl">I've<br>Been There Too</span></h2>
    <p>I know how it feels to be stuck in the 9-to-5 grind, wishing for more but not knowing how to get started. I remember my days of working long hours in a cubicle making someone rich.</p>
    <p>But I learned that success isn't about paying your self over decades hoping to get rich. <b>Its about locking in for a sprint, 90 days of laser focus can completely change your life.</b> That's how I did it. That's why I created this 90-Day step-by-step program to help people like YOU launch a brand confidently, even if you're starting from scratch.</p>
    <span class="more">Read More</span>
  </div>
  <div class="collage ph" role="img" aria-label="Coach standing beside a luxury car outdoors"></div>
</section>

<section class="trans">
  <div class="lead">
    <h2 style="font-size:18px">Here's The<br>Transformation<br><span class="hl">You'll Experience:</span></h2>
    <p>By the end of this program, you'll:</p>
    <span class="btn">Learn More</span>
  </div>
  <div class="cols">
    <div><svg class="tick" viewBox="0 0 10 10"><path d="M1.5 5.2 4 7.5 8.5 2.5" stroke="#f5a01a" fill="none" stroke-width="1.5"/></svg>Have a fully launched business that generates real income</div>
    <div><svg class="tick" viewBox="0 0 10 10"><path d="M1.5 5.2 4 7.5 8.5 2.5" stroke="#f5a01a" fill="none" stroke-width="1.5"/></svg>Feel confident and clear about your business strategy and next steps</div>
    <div><svg class="tick" viewBox="0 0 10 10"><path d="M1.5 5.2 4 7.5 8.5 2.5" stroke="#f5a01a" fill="none" stroke-width="1.5"/></svg>Have secured your first paying customers AND know exactly how to find more</div>
    <div><svg class="tick" viewBox="0 0 10 10"><path d="M1.5 5.2 4 7.5 8.5 2.5" stroke="#f5a01a" fill="none" stroke-width="1.5"/></svg>Gain the tools and knowledge to continue growing your business long after the sprint is over</div>
    <div><svg class="tick" viewBox="0 0 10 10"><path d="M1.5 5.2 4 7.5 8.5 2.5" stroke="#f5a01a" fill="none" stroke-width="1.5"/></svg>Go from struggling with ideas to running a profitable business in just 3 months</div>
    <div><svg class="tick" viewBox="0 0 10 10"><path d="M1.5 5.2 4 7.5 8.5 2.5" stroke="#f5a01a" fill="none" stroke-width="1.5"/></svg>Be one step closer to financial freedom and building generational wealth</div>
    <div><svg class="tick" viewBox="0 0 10 10"><path d="M1.5 5.2 4 7.5 8.5 2.5" stroke="#f5a01a" fill="none" stroke-width="1.5"/></svg>Save countless hours by following a proven roadmap instead of trial and error</div>
    <div><svg class="tick" viewBox="0 0 10 10"><path d="M1.5 5.2 4 7.5 8.5 2.5" stroke="#f5a01a" fill="none" stroke-width="1.5"/></svg>No fluff. No gimmicks. Just real results</div>
  </div>
  <div class="enroll"><span class="pill">Join Now</span><span>Enrollment closes soon. Secure your spot now and start building your future!<br>Join now for <b>50% OFF</b> today</span></div>
</section>

<section class="wins">
  <h2>Real People, Real Wins:<br><span class="hl">See What's Possible When You Take Action</span></h2>
  <div class="cards4">
    <div class="c feat"><p>"Renata had a fashion idea sitting in a notebook for years. After 90 days she launched her online shop and earned her first $8,000 in sales."</p><div class="rm">Read More →</div><div class="who"><i></i>"Renata"</div></div>
    <div class="c"><p>"I had the idea in my head for years but never knew where to start. After week three I had customers and closed $5,000 in sales from my new service."</p><div class="rm">Read More →</div><div class="who"><i></i>"Corey"</div></div>
    <div class="c"><p>"I've been mentored by many people but none gave me a plan this clear. My monthly income from the brand now covers all my bills."</p><div class="rm">Read More →</div><div class="who"><i></i>"Tamsin"</div></div>
    <div class="c"><p>"I had been a stay-at-home mom for a decade. The program helped me grow my business from zero to a steady income stream."</p><div class="rm">Read More →</div><div class="who"><i></i>"Priya"</div></div>
  </div>
</section>

<section class="future">
  <div class="copy">
    <h2>Future!<br><span style="color:var(--sky)">Join Now for</span> <span class="or">50% OFF button</span></h2>
    <div class="sub">Enrollment closes soon. Secure your spot now and start<br>building your future!</div>
    <span class="btn" style="border-radius:12px">Add to Cart</span><span class="outline">Join Now</span>
  </div>
  <div class="banner" role="img" aria-label="Program banner with the two coaches"></div>
</section>

<section class="killers">
  <div class="lead">
    <h2 style="font-size:16px">There are 3 Killers <span class="hl">Of<br>A Great Business:</span></h2>
    <p>Find out why businesses fail and master the strategies to overcome challenges and succeed faster than ever!</p>
  </div>
  <div class="photo" role="img" aria-label="Female coach waving, standing on an orange arc"></div>
  <div class="list">
    <h4>END HABIT #1: OVERTHINKING THE FIRST STEP</h4>
    <p>Overplanning, researching and doubting every little detail. But the longer you overthink, the longer you delay taking real action.</p>
    <h4 class="b">END HABIT #2: WAITING FOR THE "PERFECT" TIME</h4>
    <p>You tell yourself you'll start when you have more time, money or confidence. The truth? The "perfect" moment doesn't exist.</p>
    <h4>END HABIT #3: AVOIDING SALES AND MARKETING</h4>
    <p>The best products still fail if nobody hears about them. Learn to share your offer with confidence and actually make sales.</p>
  </div>
</section>

<section class="coaches pale">
  <h2 style="font-size:16px">Meet Your<br><span class="hl">&nbsp;&nbsp;&nbsp;&nbsp;Coaches</span></h2>
  <div class="pics">
    <div class="ph" role="img" aria-label="Both coaches in a studio"></div>
    <div class="ph" role="img" aria-label="Both coaches smiling together"></div>
  </div>
  <span class="tag" style="left:445px;top:60px">Meet Dana Reyes</span>
  <div class="side" role="img" aria-label="Portrait of coach Dana Reyes"></div>
</section>
<section class="bio">
  <div><h5>#1 National Bestseller List</h5><p>#1 bestselling author of seven books, which have sold over 3 million copies across 20 countries, with 20 years of expertise in health and wellness.</p><h5>Featured Nutrition Expert</h5><p>Featured nutrition expert on top TV programs including daytime talk shows and national morning news.</p></div>
  <div><h5>Personal Brand Leader</h5><p>Personal brand leader with 2.7+ million followers across social media platforms, demonstrating engagement.</p><h5>Published Thought Leader</h5><p>Published thought leader in several magazines and national outlets.</p></div>
  <div><h5>Co-Founder</h5><p>Co-founder of a thriving health supplement business, generating $40 million in revenue within five years.</p><h5>Proven Business Strategist</h5><p>Proven business strategist, leveraging her expertise to grow brands and guide others to success.</p></div>
</section>
<section class="todd">
  <div class="photo" role="img" aria-label="Coach Marcus Hale walking in a dark suit"></div>
  <div class="txt">
    <span class="tag" style="left:10px;top:18px">Meet Marcus "MH" Hale</span>
    <div class="grid">
      <div>
        <h5>Founder and CEO</h5><p>Founder and CEO of a high-performing IT consulting firm, achieving over $65 million in annual revenue and successfully selling the company for 8 figures after 11 years of leadership.</p>
        <h5>Co-Founder</h5><p>Co-founder of a health supplement business, generating $40 million in revenue within five years and serving over 450,000 customers globally.</p>
        <h5>Shaped the Global Success of Dana Reyes's 7 books</h5><p>Shaped the global success of Dana Reyes's books, marketing negotiations and marketing efforts that have driven over 3 million copies sold.</p>
      </div>
      <div>
        <h5>Entrepreneur with 30+ Years of Expertise</h5><p>Entrepreneur with 30+ years of expertise building and scaling successful ventures across diverse industries, including IT, retail, information marketing and publishing, hospitality and commercial construction.</p>
        <h5>Recognized by Venture Weekly</h5><p>Recognized as a founder of one of the fastest-growing information technology companies, showcasing exceptional growth and innovation.</p>
        <h5>Secured multiple seven-figure book deals</h5><p>Secured multiple seven-figure book deals, cementing the brand's status as an influential publishing and global brand.</p>
      </div>
    </div>
  </div>
</section>
<section class="media"><i></i><i></i><i></i><i></i><i></i><i></i><i></i><i></i></section>

<section class="inspire pale" style="padding:18px 0 0">
  <div class="strip">
    <div role="img" aria-label="Coaches at a media event"></div>
    <div role="img" aria-label="Coach with guests on a TV set"></div>
    <div role="img" aria-label="Coach in red dress on stage"></div>
    <div role="img" aria-label="Coaches with a talk show host"></div>
    <div role="img" aria-label="Coaches at a book signing"></div>
  </div>
  <h2><span class="or">Be Inspired:</span> How People Just Like You<br><span class="sm">Built Wealth and Freedom</span></h2>
  <div class="cards3">
    <div class="c"><div class="av" role="img" aria-label="Member portrait"></div><b>Renata</b><p>"I was a senior accountant who dreamed of owning a firm. I now run my own practice with twelve clients and growing."</p><span class="rm">Read More →</span></div>
    <div class="c"><div class="av" role="img" aria-label="Member portrait"></div><b>Corey</b><p>"I managed my 9-to-5 while launching a consulting brand. I never thought it could happen this fast."</p><span class="rm">Read More →</span></div>
    <div class="c"><div class="av" role="img" aria-label="Member portrait"></div><b>Tamsin</b><p>"I doubted myself on everything. The daily steps kept me moving and now my products sell every week."</p><span class="rm">Read More →</span></div>
  </div>
</section>

<section class="every">
  <h2><span class="or">Here's</span> EVERYTHING YOU GET <span class="or" style="font-size:11px">with</span><br><span class="sm" style="font-size:11px">the Harvest Ledger Method Course:</span></h2>
  <div class="grid4">
    <div>
      <div class="it"><svg class="tick" viewBox="0 0 10 10"><path d="M1.5 5.2 4 7.5 8.5 2.5" stroke="#f5a01a" fill="none" stroke-width="1.5"/></svg><div><b>A Fully Launched Business</b><p>By day 90 you'll have a live business generating income on your terms.</p></div></div>
      <div class="it"><svg class="tick" viewBox="0 0 10 10"><path d="M1.5 5.2 4 7.5 8.5 2.5" stroke="#f5a01a" fill="none" stroke-width="1.5"/></svg><div><b>Paying Customers in Hand</b><p>You'll have secured your first paying customers and a plan for more.</p></div></div>
      <div class="it"><svg class="tick" viewBox="0 0 10 10"><path d="M1.5 5.2 4 7.5 8.5 2.5" stroke="#f5a01a" fill="none" stroke-width="1.5"/></svg><div><b>The 90-Day Business Blueprint</b><p>A comprehensive step-by-step roadmap showing exactly what to do each week.</p></div></div>
      <div class="it"><svg class="tick" viewBox="0 0 10 10"><path d="M1.5 5.2 4 7.5 8.5 2.5" stroke="#f5a01a" fill="none" stroke-width="1.5"/></svg><div><b>Paying Customers in Hand</b><p>Learn fast sales and repeat offers that keep money coming in.</p></div></div>
    </div>
    <div>
      <div class="it"><svg class="tick" viewBox="0 0 10 10"><path d="M1.5 5.2 4 7.5 8.5 2.5" stroke="#f5a01a" fill="none" stroke-width="1.5"/></svg><div><b>Done-For-You Templates</b><p>Ready-made scripts and guides to save time and skip guesswork.</p></div></div>
      <div class="it"><svg class="tick" viewBox="0 0 10 10"><path d="M1.5 5.2 4 7.5 8.5 2.5" stroke="#f5a01a" fill="none" stroke-width="1.5"/></svg><div><b>Essential AI Training</b><p>Harness the power of AI to transform your business, from content to customer support and marketing.</p></div></div>
      <div class="it"><svg class="tick" viewBox="0 0 10 10"><path d="M1.5 5.2 4 7.5 8.5 2.5" stroke="#f5a01a" fill="none" stroke-width="1.5"/></svg><div><b>Proven and Repeatable Systems</b><p>Turn your ideas into steady results with systems that work again and again.</p></div></div>
      <div class="it"><svg class="tick" viewBox="0 0 10 10"><path d="M1.5 5.2 4 7.5 8.5 2.5" stroke="#f5a01a" fill="none" stroke-width="1.5"/></svg><div><b>Scalable Growth Roadmap</b><p>A blueprint for scaling beyond your launch into lasting success.</p></div></div>
    </div>
    <div>
      <div class="it"><svg class="tick" viewBox="0 0 10 10"><path d="M1.5 5.2 4 7.5 8.5 2.5" stroke="#f5a01a" fill="none" stroke-width="1.5"/></svg><div><b>Private Mastermind Community</b><p>You'll be surrounded by driven founders and guided for 12 and 15 extra days of live help.</p></div></div>
      <div class="it"><svg class="tick" viewBox="0 0 10 10"><path d="M1.5 5.2 4 7.5 8.5 2.5" stroke="#f5a01a" fill="none" stroke-width="1.5"/></svg><div><b>Weekly LIVE Coaching Calls and Q&amp;A Sessions</b><p>Get real answers directly from proven coaches and fellow members.</p></div></div>
    </div>
    <div>
      <div class="it"><svg class="tick" viewBox="0 0 10 10"><path d="M1.5 5.2 4 7.5 8.5 2.5" stroke="#f5a01a" fill="none" stroke-width="1.5"/></svg><div><b>Confidence in Your Business</b><p>With a clear roadmap and support, you'll have the confidence to keep growing.</p></div></div>
      <div class="it"><svg class="tick" viewBox="0 0 10 10"><path d="M1.5 5.2 4 7.5 8.5 2.5" stroke="#f5a01a" fill="none" stroke-width="1.5"/></svg><div><b>Weekly Actionable Tasks and Assignments</b><p>Clear weekly tasks keep you on track so you're always completing the right work.</p></div></div>
    </div>
  </div>
  <div class="rule"></div>
</section>

<section class="stories">
  <div class="lead">
    <h2>Real Stories, Real Results:<br><span class="hl">See How Others Transformed<br>Their Lives</span></h2>
    <p>This isn't just a course—it's a launch pad for your future business.</p>
    <div class="dates"><b>Key Dates &amp; Times</b><span>Program Length: 90 Days</span><span>Live Sessions: Weekly at 7 PM EST</span><span>Doors Close: Friday, 11:59 PM</span></div>
  </div>
  <div class="vids">
    <div class="v"><div class="thumb" role="img" aria-label="Video testimonial"><svg width="10" height="10" viewBox="0 0 10 10"><path d="M2 1 9 5 2 9z" fill="#fff"/></svg></div><div class="q">"I've made more money from this course than I ever did at my last job"<br><span>Watch Video</span></div></div>
    <div class="v"><div class="thumb" role="img" aria-label="Video testimonial"><svg width="10" height="10" viewBox="0 0 10 10"><path d="M2 1 9 5 2 9z" fill="#fff"/></svg></div><div class="q">"This changed my life and taught me the basics"<br><span>Watch Video</span></div></div>
    <div class="v"><div class="thumb" role="img" aria-label="Video testimonial"><svg width="10" height="10" viewBox="0 0 10 10"><path d="M2 1 9 5 2 9z" fill="#fff"/></svg></div><div class="q">"I doubted myself on everything and now our business brings in real profit"<br><span>Watch Video</span></div></div>
  </div>
</section>

<section class="types">
  <div class="wheelcard">
    <h6>WHAT TYPE OF BUSINESS CAN I LAUNCH IN 90 DAYS?</h6>
    <svg width="370" height="240" viewBox="0 0 370 240" font-family="Montserrat, sans-serif" font-size="5" fill="#1f2a3a">
      <g fill="none" stroke-width="6">
        <circle cx="185" cy="120" r="48" stroke="#2b9be0" stroke-dasharray="36 2" />
      </g>
      <g fill="none" stroke-width="6" transform="rotate(45 185 120)">
        <circle cx="185" cy="120" r="48" stroke="#f5a01a" stroke-dasharray="36 116" />
      </g>
      <g fill="none" stroke-width="6" transform="rotate(180 185 120)">
        <circle cx="185" cy="120" r="48" stroke="#e6457a" stroke-dasharray="36 264" />
      </g>
      <circle cx="185" cy="120" r="22" fill="#fff" stroke="#cfd8e3"/>
      <g fill="#fff" stroke="#9aa6b5">
        <circle cx="185" cy="84" r="7"/><circle cx="211" cy="95" r="7"/><circle cx="221" cy="120" r="7"/><circle cx="211" cy="145" r="7"/>
        <circle cx="185" cy="156" r="7"/><circle cx="159" cy="145" r="7"/><circle cx="149" cy="120" r="7"/><circle cx="159" cy="95" r="7"/>
      </g>
      <text x="100" y="34" font-weight="700">Community &amp; Membership</text>
      <text x="235" y="34" font-weight="700">Service-Based Businesses</text>
      <text x="40" y="78" font-weight="700">Technology &amp; Online Tools</text>
      <text x="265" y="80" font-weight="700">Digital Product Creation</text>
      <text x="45" y="170" font-weight="700">Health &amp; Wellness</text>
      <text x="262" y="168" font-weight="700">E-Commerce &amp; Product</text>
      <text x="155" y="218" font-weight="700">Content &amp; Personal Brands</text>
    </svg>
  </div>
  <div class="note">Do you like to work with people, teach skills, sell online or create content? There's a business model for you, and we'll help you choose the right one to launch.</div>
</section>

<section class="faq pale">
  <div class="list">
    <h3>Frequently Asked Questions</h3>
    <b>What if I don't have a business idea yet?</b><p>No problem! The course will guide you through brainstorming and validating a profitable idea.</p>
    <b>Do I need a lot of money to start?</b><p>Nope! We focus on strategies that require minimal upfront investment.</p>
    <b>What if I'm super busy with my 9-to-5?</b><p>This course is designed for busy professionals with schedules that you can complete during the course sessions.</p>
    <b>How long will it take for me to see results?</b><p>Most participants secure their first paying customers within 30 days, and by the end of 90 days they have a fully launched business.</p>
  </div>
  <div class="fcard"><div class="img" role="img" aria-label="Female coach in a red dress"></div><div class="date">Dec<br>13</div><b>Is this also for people who work full-time?</b><p>Yes! The course is perfect for busy people →</p></div>
  <div class="fcard"><div class="img" role="img" aria-label="Male coach in a studio" style="background:linear-gradient(160deg,#e0ddd8,#4a4650)"></div><div class="date">Dec<br>13</div><b>If I don't like it, can I request a refund?</b><p>Yes. If you follow the steps and see no progress we'll make it right.</p></div>
</section>

<section class="cta">
  <h2>Are you ready to finally launch your<br>business and start making real money?</h2>
  <h3>Join Now for 50% OFF<br>Today's Special Registration Price: $999 or (Was $1,999)</h3>
  <span class="btn">Add to Cart</span>
  <p>Pay in full or pay OR<br>Buy Now, Pay Later with EasySplit which allows you to choose a flexible payment plan</p>
  <div class="yes">YES! I'm Ready!</div>
</section>

<section class="foot pale">
  <div class="row">
    <div class="banner" role="img" aria-label="Program banner with the two coaches"></div>
    <div>
      <h4>Address</h4>
      <p>Company 795 12th Street, Office 478 US,<br>DA 81566</p>
      <div class="soc"><i></i><i></i><i></i><i></i></div>
    </div>
    <div>
      <h4>Say Hello</h4>
      <div class="contact"><svg width="8" height="8" viewBox="0 0 10 10"><path d="M2 1h2l1 2.5-1.3 1a6 6 0 0 0 2.8 2.8l1-1.3L10 7v2a1 1 0 0 1-1 1A8 8 0 0 1 0 2a1 1 0 0 1 1-1z" fill="#e6457a"/></svg>+0 123 456 789 0</div>
      <div class="contact"><svg width="8" height="8" viewBox="0 0 10 10"><rect x="0.5" y="2" width="9" height="6.5" fill="#e6457a"/><path d="M0.5 2 5 6l4.5-4" stroke="#fff" fill="none" stroke-width=".8"/></svg>name@example.com</div>
    </div>
  </div>
  <div class="legal"><div><span>Home</span><span>Services ▾</span><span>Contact</span><span>About Us</span><span>FAQs</span></div><div>Copyright © 2025 All Rights Reserved</div></div>
</section>

</div>
</body>
</html>
```